Business cards for a naturopathic day clinic for stem cell therapy

We need a basic design for a day clinic, that offers stem cell therapies for Lyme therapy and other severe chronic illnesses.
Our name is "Casa velorìn", which can be translated into "Manor Velorbloom". We are a couple of naturopaths working along side physiotherapists and osteopaths, yoga teachers and massage therapists. I attached our logo.

```html
<!DOCTYPE html>
<html lang="en">
<head>
<meta charset="utf-8">
<title>Casa velorìn – Business Cards</title>
<link href="https://fonts.googleapis.com/css2?family=Montserrat:wght@300;400;600&display=swap" rel="stylesheet">
<style>
  :root {
    --stage: #2a2a2a;
    --card-dark: #141414;
    --leaf: #b8c660;
    --leaf-soft: #c6d27c;
    --taupe: #a39283;
    --white: #ffffff;
    --rule: #2c2c2c;
  }
  * { margin: 0; padding: 0; box-sizing: border-box; }
  html, body {
    width: 1200px; height: 866px; overflow: hidden;
    background: var(--stage);
    font-family: "Montserrat", Arial, sans-serif;
  }
  .stage {
    position: relative; width: 1200px; height: 866px;
  }
  .card {
    position: absolute;
    width: 510px; height: 292px;
    top: 287px;
    box-shadow: 0 14px 30px rgba(0,0,0,0.45);
    overflow: hidden;
  }
  .card--front { left: 60px; background: var(--leaf); }
  .card--back { left: 630px; background: var(--card-dark); }

  .brand {
    position: absolute;
    display: flex; align-items: center; gap: 14px;
  }
  .brand__dot {
    width: 46px; height: 46px; border-radius: 50%;
  }
  .brand__name {
    font-weight: 300; letter-spacing: 1px; white-space: nowrap;
  }
  .card--front .brand { left: 100px; top: 118px; }
  .card--front .brand__dot { background: var(--white); }
  .card--front .brand__name { color: var(--white); font-size: 44px; }

  .card--back .brand { left: 250px; top: 58px; gap: 10px; }
  .card--back .brand__dot { width: 34px; height: 34px; background: var(--leaf); }
  .card--back .brand__name { color: var(--leaf); font-size: 30px; }

  .contact {
    position: absolute; left: 34px; top: 40px;
  }
  .contact__name {
    color: var(--leaf); font-weight: 600; font-size: 19px; letter-spacing: 0.3px;
  }
  .contact__role {
    color: var(--taupe); font-size: 12px; margin-top: 2px; margin-bottom: 12px;
  }
  .contact__line {
    display: flex; align-items: center; gap: 7px;
    color: var(--taupe); font-size: 11.5px; line-height: 18px;
  }
  .contact__line svg { width: 11px; height: 11px; flex: none; }

  .rule {
    position: absolute; left: 250px; right: 30px; top: 150px;
    height: 1px; background: var(--rule);
  }
  .address {
    position: absolute; right: 34px; bottom: 36px;
    color: var(--taupe); font-size: 12px; line-height: 18px; text-align: right;
  }
</style>
</head>
<body>
<main class="stage">
  <section class="card card--front" aria-label="Card front">
    <div class="brand">
      <span class="brand__dot"></span>
      <span class="brand__name">Casa velorìn</span>
    </div>
  </section>

  <section class="card card--back" aria-label="Card back">
    <div class="contact">
      <p class="contact__name">Elena Marwick</p>
      <p class="contact__role">Managing Director</p>
      <p class="contact__line">
        <svg viewBox="0 0 12 12"><path d="M2.5 1.2l2 0 .8 2.4-1.2.9a6 6 0 0 0 3.4 3.4l.9-1.2 2.4.8 0 2a1 1 0 0 1-1 1A9 9 0 0 1 1.5 2.2a1 1 0 0 1 1-1z" fill="var(--leaf)"/></svg>
        031-555 208 416
      </p>
      <p class="contact__line">
        <svg viewBox="0 0 12 12"><rect x="0.5" y="2.5" width="11" height="7.5" fill="var(--leaf)"/><path d="M0.8 2.8L6 7l5.2-4.2" stroke="var(--card-dark)" stroke-width="1" fill="none"/></svg>
        hello@velorin-care.com
      </p>
      <p class="contact__line">
        <svg viewBox="0 0 12 12"><circle cx="6" cy="6" r="5" fill="none" stroke="var(--leaf)" stroke-width="1.2"/><path d="M1 6h10M6 1c-2.5 3-2.5 7 0 10M6 1c2.5 3 2.5 7 0 10" stroke="var(--leaf)" stroke-width="1" fill="none"/></svg>
        www.velorin-care.com
      </p>
    </div>

    <div class="brand">
      <span class="brand__dot"></span>
      <span class="brand__name">Casa velorìn</span>
    </div>

    <div class="rule"></div>

    <p class="address">17, Linden Orchard Lane<br>60314, Aldermere</p>
  </section>
</main>
</body>
</html>
```